Business Cards for Tomas and Welby

Design of business cards for two people with the recently created brand Caldor Mobile. Caldor Mobile wants to become a worldwide major player on the secondhand phone market. It gathers send hand phones from individuals, refurbish them and sell them throughout the world. It has a green impact (recycling) and we also contribute to social project in Africa (a percentage of our benefits are sent to build school, sport facilities, etc.

Target Market(s)

B2B - Tomas and Welby are in contact with distributors across Africa.

Industry/Entity Type

Wireless Communication

Contact Information for Business Card

Tomas Vireaux
Head of Emerging Markets
Caldor Energy South Africa (Pty) Ltd
Fennick Street 47
2031 Sandton - Johannesburg
South Africa
Tel: + 27 10 555 0184
Mobile : +27 82 55 017
Email : tomas.vireaux@caldormobile.example
Skype: tomas.vireaux
Web: www.caldormobile.example
 

Welby Crofts
Head of Southern Africa
Fennick Street 47
South Africa
Tel: + 27 10 555 0184
Mobile: +27 83 555 0297
Email: welby.crofts@caldormobile.example
Skype: welby.crofts
Web: www.caldormobile.example

Requirements
Must have
• The cards need to be "serious", trustable, with a worldwide presence.
Nice to have
• Some "green" / recycling touch would be nice but not necessary if in contradiction with the general design.

```html
<!DOCTYPE html>
<html lang="en">
<head>
<meta charset="utf-8">
<title>Caldor Mobile – Business Card, Welby Crofts</title>
<link href="https://fonts.googleapis.com/css2?family=Open+Sans:wght@400;600;700&display=swap" rel="stylesheet">
<style>
  :root {
    --backdrop: #1c1c1c;
    --brand-blue: #2f97d6;
    --brand-blue-light: #3fa5de;
    --brand-navy: #11314f;
    --text-grey: #555a60;
    --rule-grey: #9a9ea3;
    --card-white: #ffffff;
  }
  * { box-sizing: border-box; margin: 0; padding: 0; }
  html, body {
    width: 1200px; height: 960px; overflow: hidden;
    background: var(--backdrop);
    font-family: "Open Sans", Arial, sans-serif;
  }
  .canvas { position: relative; width: 1200px; height: 960px; }
  .card {
    position: absolute; left: 250px; width: 700px; height: 400px;
    box-shadow: 0 10px 30px rgba(0,0,0,.5);
  }
  .card-front {
    top: 60px;
    background: radial-gradient(circle at 55% 45%, var(--brand-blue-light), var(--brand-blue) 75%);
    display: flex; align-items: center; justify-content: center;
  }
  .wordmark {
    display: flex; align-items: center; gap: 14px;
    font-weight: 700; letter-spacing: -0.5px;
  }
  .wordmark-dot { border-radius: 50%; flex: none; }
  .card-front .wordmark { color: var(--card-white); font-size: 52px; }
  .card-front .wordmark-dot { width: 34px; height: 34px; background: var(--card-white); }

  .card-back { top: 500px; background: var(--card-white); }
  .card-back .wordmark {
    position: absolute; left: 40px; top: 178px;
    color: var(--brand-navy); font-size: 34px;
  }
  .card-back .wordmark-dot { width: 24px; height: 24px; background: var(--brand-navy); }
  .divider {
    position: absolute; left: 340px; top: 110px; width: 1px; height: 190px;
    background: var(--rule-grey);
  }
  .contact { position: absolute; left: 368px; top: 108px; color: var(--text-grey); }
  .person-name { font-size: 22px; font-weight: 700; color: var(--brand-navy); line-height: 1.1; }
  .person-role { font-size: 15px; color: var(--brand-blue); margin-bottom: 14px; }
  .address { font-size: 14px; line-height: 1.4; margin-bottom: 12px; }
  .lines { list-style: none; font-size: 14px; line-height: 1.45; }
  .lines li { display: flex; align-items: center; gap: 8px; }
  .lines svg { width: 12px; height: 12px; flex: none; fill: var(--brand-blue); }
</style>
</head>
<body>
<div class="canvas">
  <section class="card card-front">
    <div class="wordmark"><span class="wordmark-dot"></span><span>Caldor Mobile</span></div>
  </section>

  <section class="card card-back">
    <div class="wordmark"><span class="wordmark-dot"></span><span>Caldor Mobile</span></div>
    <div class="divider"></div>
    <div class="contact">
      <p class="person-name">Welby Crofts</p>
      <p class="person-role">Head of Southern Africa</p>
      <p class="address">Fennick Street 47, 2031 Sandton<br>Johannesburg, South Africa</p>
      <ul class="lines">
        <li><svg viewBox="0 0 12 12"><path d="M2.5 1l2 2.2-1 1.3c.7 1.5 1.8 2.6 3.3 3.3l1.3-1 2.2 2-1.2 1.7C5 10.3 1.7 7 .8 2.2z"/></svg>+ 27 10 555 0184</li>
        <li><svg viewBox="0 0 12 12"><path d="M3 0h6v12H3zM4 1.5v8h4v-8z"/></svg>+27 83 555 0297</li>
        <li><svg viewBox="0 0 12 12"><path d="M0 2h12v8H0zM1 3l5 3.5L11 3v-.2H1z"/></svg>welby.crofts@caldormobile.example</li>
        <li><svg viewBox="0 0 12 12"><circle cx="6" cy="6" r="5.5"/></svg>welby.crofts</li>
        <li><svg viewBox="0 0 12 12"><path d="M6 0a6 6 0 100 12A6 6 0 006 0zm0 1.2c.7.8 1.2 2 1.3 3.3H4.7C4.8 3.2 5.3 2 6 1.2zM1.3 5.5h2.4c0 1.3.3 2.5.9 3.5A4.8 4.8 0 011.3 5.5zm3.4 0h2.6c-.1 1.3-.6 2.5-1.3 3.3-.7-.8-1.2-2-1.3-3.3zm3.6 0h2.4a4.8 4.8 0 01-3.3 3.5c.6-1 .9-2.2.9-3.5z"/></svg>www.caldormobile.example</li>
      </ul>
    </div>
  </section>
</div>
</body>
</html>
```